PPT template for boutique strategic planning, accounting and taxation firm

We are a boutique firm that provides strategic, accounting and tax advice to our clients. The work we are doing is increasingly strategic work and we are required to produce reports and presentations and our current templates are simply not sufficient.
As you can see from the examples attached, we have very limited skills in house re design! We have attached a PPT document and word document (that should be PPT) that we use regularly as examples of the content. Excel worksheets are regularly embedded into the presentation (in both blue and orange - see below re colours)
Not specific to one area but typically these clients are famous for their own brand and are creating value in their industry through creating their own brand and we want to produce documents of a similar standard.
A Powerpoint Document Slide Template
Cover page layout, back page, intermediate page heading, in colours and styles based on the logo, title styles, and an intermediate or chapter heading slide style. Many of our presentations contain slides with tables, diagrams, flowcharts and text, including simple lists of bullet points. As above, you will see in our style guide that we have three coloured logos – we would like one version in blue and one version in orange please. Again, the cover should be bold and draw attention but remain professional.
We are looking for something that works in both 4:3 and 16:9 (or two templates please)
We like a clear professional and simple look.
Deliverable: PowerPoint template file (.potx extension) for PowerPoint 2007 with at least a “cover” layout, a “title and content” layout, and a simplified slide layout, as well as “back cover”. Please embed any fonts used.
Target Market(s)
Many of our clients are retail clients or have strong brands of their own.
Industry/Entity Type
Accounting
Requirements
Must have
- Harrowby & Co logo on each page.
Must have a cover page (please be bold but professional)
A selection of "standard" slides - dot points, detailed written content, example diagrams, flow charts etc.
A back cover
Nice to have
- We would like to have a copy done in both the blue and orange versions attached. Happy for the winner to complete the other colour after the winner is selected.
Prefer Arial logo but open to suggestions. Must be easy to read and professional
Should not have
- Nothing cartoonish

```html
<!DOCTYPE html>
<html lang="en">
<head>
<meta charset="utf-8">
<title>Harrowby &amp; Co – Presentation Template Covers</title>
<link href="https://fonts.googleapis.com/css2?family=Arimo:wght@400;700&display=swap" rel="stylesheet">
<style>
  :root {
    --ink: #474c57;
    --orange: #f47c20;
    --blue: #0563b0;
    --teal: #4aacc5;
    --paper: #ffffff;
    --canvas: #ffffff;
  }
  * { box-sizing: border-box; margin: 0; padding: 0; }
  html, body {
    width: 1200px; height: 1000px; overflow: hidden;
    background: var(--canvas);
    font-family: "Arimo", Arial, sans-serif;
  }
  .board { position: relative; width: 1200px; height: 1000px; }

  .slide {
    position: absolute;
    background: var(--paper);
    overflow: hidden;
    box-shadow: 2px 3px 4px rgba(0,0,0,0.35);
    border: 1px solid #c9c9c9;
  }
  .slide--brand { left: 0; width: 578px; height: 328px; }
  .slide--cover { left: 605px; width: 583px; height: 324px; }

  .sidebar { position: absolute; top: 0; left: 0; bottom: 0; background: var(--ink); }
  .slide--brand .sidebar { width: 158px; }
  .slide--cover .sidebar { width: 192px; }
  .sidebar--teal { background: var(--teal); }

  /* Brand lockup */
  .lockup { position: absolute; left: 100px; top: 110px; display: flex; align-items: center; }
  .lockup__mark { width: 108px; height: 108px; border-radius: 50%; flex: none; }
  .lockup__text { margin-left: 14px; }
  .lockup__name {
    font-weight: 700; font-size: 46px; line-height: 1; color: var(--ink);
    letter-spacing: -0.5px; white-space: nowrap;
  }
  .lockup__tagline {
    margin-top: 10px; font-weight: 700; font-size: 13px; color: var(--ink); white-space: nowrap;
  }

  /* Cover */
  .badge {
    position: absolute; left: 44px; top: 77px;
    width: 174px; height: 174px; border-radius: 50%;
  }
  .cover-title { position: absolute; left: 3px; top: 128px; color: #fff; }
  .cover-title__kicker {
    position: absolute; left: 86px; top: 4px;
    font-weight: 700; font-size: 17px; white-space: nowrap;
  }
  .cover-title__main {
    position: absolute; left: 0; top: 20px;
    font-size: 60px; line-height: 1; letter-spacing: -1px; white-space: nowrap;
  }
  .cover-client {
    position: absolute; left: 298px; top: 148px;
    font-size: 30px; color: var(--ink); white-space: nowrap;
  }
  .footer-bar { position: absolute; left: 0; top: 290px; width: 430px; height: 30px; }
  .footer-logo { position: absolute; left: 428px; top: 288px; display: flex; align-items: center; }
  .footer-logo__mark { width: 32px; height: 32px; border-radius: 50%; flex: none; }
  .footer-logo__text { margin-left: 5px; }
  .footer-logo__name { font-weight: 700; font-size: 15px; color: var(--ink); line-height: 1; white-space: nowrap; }
  .footer-logo__tagline { font-size: 5px; color: var(--ink); white-space: nowrap; margin-top: 2px; }

  .fill-orange { background: var(--orange); }
  .fill-blue { background: var(--blue); }
</style>
</head>
<body>
<main class="board">

  <!-- Orange set -->
  <section class="slide slide--brand" style="top:2px">
    <div class="sidebar"></div>
    <div class="lockup">
      <span class="lockup__mark fill-orange"></span>
      <div class="lockup__text">
        <div class="lockup__name">Harrowby &amp; Co</div>
        <div class="lockup__tagline">Accounting, Taxation &amp; Strategic Business Advisors</div>
      </div>
    </div>
  </section>
  <section class="slide slide--cover" style="top:8px">
    <div class="sidebar"></div>
    <span class="badge fill-orange"></span>
    <h1 class="cover-title"><span class="cover-title__kicker">Strategic</span><span class="cover-title__main">Review</span></h1>
    <p class="cover-client">Company Name</p>
    <div class="footer-bar fill-orange"></div>
    <div class="footer-logo">
      <span class="footer-logo__mark fill-orange"></span>
      <div class="footer-logo__text">
        <div class="footer-logo__name">Harrowby &amp; Co</div>
        <div class="footer-logo__tagline">Accounting, Taxation &amp; Strategic Business Advisors</div>
      </div>
    </div>
  </section>

  <!-- Blue set -->
  <section class="slide slide--brand" style="top:335px">
    <div class="sidebar"></div>
    <div class="lockup">
      <span class="lockup__mark fill-blue"></span>
      <div class="lockup__text">
        <div class="lockup__name">Harrowby &amp; Co</div>
        <div class="lockup__tagline">Accounting, Taxation &amp; Strategic Business Advisors</div>
      </div>
    </div>
  </section>
  <section class="slide slide--cover" style="top:338px">
    <div class="sidebar"></div>
    <span class="badge fill-blue"></span>
    <h1 class="cover-title"><span class="cover-title__kicker">Strategic</span><span class="cover-title__main">Review</span></h1>
    <p class="cover-client">Company Name</p>
    <div class="footer-bar fill-blue"></div>
    <div class="footer-logo">
      <span class="footer-logo__mark fill-blue"></span>
      <div class="footer-logo__text">
        <div class="footer-logo__name">Harrowby &amp; Co</div>
        <div class="footer-logo__tagline">Accounting, Taxation &amp; Strategic Business Advisors</div>
      </div>
    </div>
  </section>

  <!-- Teal set -->
  <section class="slide slide--brand" style="top:668px">
    <div class="sidebar sidebar--teal"></div>
    <div class="lockup">
      <span class="lockup__mark fill-orange"></span>
      <div class="lockup__text">
        <div class="lockup__name">Harrowby &amp; Co</div>
        <div class="lockup__tagline">Accounting, Taxation &amp; Strategic Business Advisors</div>
      </div>
    </div>
  </section>
  <section class="slide slide--cover" style="top:668px">
    <div class="sidebar sidebar--teal"></div>
    <span class="badge fill-orange"></span>
    <h1 class="cover-title"><span class="cover-title__kicker">Strategic</span><span class="cover-title__main">Review</span></h1>
    <p class="cover-client">Company Name</p>
    <div class="footer-bar fill-orange"></div>
    <div class="footer-logo">
      <span class="footer-logo__mark fill-orange"></span>
      <div class="footer-logo__text">
        <div class="footer-logo__name">Harrowby &amp; Co</div>
        <div class="footer-logo__tagline">Accounting, Taxation &amp; Strategic Business Advisors</div>
      </div>
    </div>
  </section>

</main>
</body>
</html>
```